creation of business cards for Velmora Sàrl

Velmora S% 26 # 224; rl is a soci% 26 # 233; t% 26 # 233; consultancy that accompanies companies in the development of their business on the market% 26 # 233; Switzerland by providing strategic contacts or market information; and by providing administrative or logistical support. Our consulting skills focus on sectors% 26 # 224; high value added% 26 # 233; e, such as trade in food goods% 26 # 39amp; drinks, fashion% 26amp; lifestyle, products and services for% 26 # 233; s in high-tech industries (pharmaceutical, chemical, m% 26 # 233; pricy 26% 23 #; cision) or sustainable solutions (% 26 # 233; energies renewable, mat% 26 # 233; recyclable materials). As part of the launch of our activity% 26 # 233;, we need% 26 # 39;% 26 # 233; to establish business cards to d% 26 # 233; work our new customers (Swiss or international).

Target Market(s)

Companies wishing to develop their activity% 26 # 233; s in Switzerland or% 26 # 224; l% 26 # 39;% 26 # 233; abroad (mainly in Europe).

Contact Information for Business Card

Prénom NOM
Velmora Sàrl
Bureau de Lavertin
Rue des Tilleuls 14, 2000 Neuchâtel
Tél. : 032 718 46 39
info@velmora-conseil.ch
www.velmora-conseil.ch

Font styles to use
Serif
Sans Serif

Colors

Designer to choose colors to be used in the design.

Requirements
Must have
• The logo The name of the company% 26 # 233; t% 26 # 233; (Velmora S% 26 # 224; rl) One field for the mailing address One field for the number% 26 # 233; ro de t% 26 # 233; l% 26 # 233; phone One field for the % 26 # 39; email address and website

```html
<!DOCTYPE html>
<html lang="fr">
<head>
<meta charset="utf-8">
<title>Velmora Sàrl – carte de visite</title>
<link rel="stylesheet" href="https://fonts.googleapis.com/css2?family=Arimo:wght@400;700&display=swap">
<style>
  :root {
    --page: #e9ebee;
    --navy: #1b3d55;
    --steel: #aab8c6;
    --frost: #f0f1f3;
    --ink-light: #ffffff;
    --ink-dark: #1b3d55;
  }
  * { margin: 0; padding: 0; box-sizing: border-box; }
  html, body {
    width: 1200px;
    height: 900px;
    overflow: hidden;
    background: var(--page);
    font-family: "Arimo", Arial, sans-serif;
  }
  .business-card {
    position: absolute;
    left: 114px;
    top: 150px;
    width: 972px;
    height: 600px;
    border-radius: 18px;
    overflow: hidden;
    background: var(--steel);
    box-shadow: 0 10px 30px rgba(27, 61, 85, 0.18);
  }
  .card-panel {
    position: absolute;
    left: 0;
    top: 0;
    width: 683px;
    height: 100%;
    background: var(--navy);
  }
  .holder-name {
    position: absolute;
    left: 56px;
    top: 100px;
    font-size: 33px;
    font-weight: 700;
    letter-spacing: 0.5px;
    color: var(--ink-light);
    line-height: 1;
  }
  .contact-list {
    position: absolute;
    left: 56px;
    top: 186px;
    list-style: none;
    color: var(--ink-light);
    font-size: 26px;
    line-height: 36px;
  }
  .contact-list li {
    display: flex;
    align-items: center;
    gap: 8px;
  }
  .contact-icon {
    width: 22px;
    height: 22px;
    flex: none;
  }
  .company-address {
    position: absolute;
    left: 56px;
    top: 344px;
    font-style: normal;
    color: var(--ink-light);
    font-size: 26px;
    line-height: 36px;
  }
  .company-name {
    font-weight: 700;
    display: block;
  }
  .brand-plate {
    position: absolute;
    left: 460px;
    top: 93px;
    width: 411px;
    height: 412px;
    border-radius: 14px;
    background: var(--frost);
    display: flex;
    align-items: center;
    justify-content: center;
  }
  .brand-name {
    font-size: 50px;
    font-weight: 400;
    letter-spacing: 4px;
    color: var(--ink-dark);
  }
</style>
</head>
<body>
  <section class="business-card">
    <div class="card-panel">
      <p class="holder-name">PRENOM NOM</p>
      <ul class="contact-list">
        <li>
          <svg class="contact-icon" viewBox="0 0 24 24" aria-hidden="true">
            <path fill="#fff" d="M6.6 10.8a15.1 15.1 0 0 0 6.6 6.6l2.2-2.2c.3-.3.7-.4 1-.2 1.1.4 2.3.6 3.6.6.6 0 1 .4 1 1V20c0 .6-.4 1-1 1A17 17 0 0 1 3 4c0-.6.4-1 1-1h3.5c.6 0 1 .4 1 1 0 1.3.2 2.5.6 3.6.1.3 0 .7-.2 1z"/>
          </svg>
          <span>032 718 46 39</span>
        </li>
        <li>
          <svg class="contact-icon" viewBox="0 0 24 24" aria-hidden="true">
            <rect x="2" y="5" width="20" height="14" rx="1.5" fill="#fff"/>
            <path d="M3 6.5l9 6.5 9-6.5" fill="none" stroke="#1b3d55" stroke-width="1.6"/>
          </svg>
          <span>info@velmora-conseil.ch</span>
        </li>
        <li>
          <svg class="contact-icon" viewBox="0 0 24 24" aria-hidden="true">
            <circle cx="12" cy="12" r="9" fill="#fff"/>
            <path d="M3 12h18M12 3c3 3 3 15 0 18M12 3c-3 3-3 15 0 18" fill="none" stroke="#1b3d55" stroke-width="1.3"/>
          </svg>
          <span>www.velmora-conseil.ch</span>
        </li>
      </ul>
      <address class="company-address">
        <span class="company-name">VELMORA SARL</span>
        Bureau de Lavertin<br>
        Rue des Tilleuls 14<br>
        2000 Neuchâtel
      </address>
    </div>
    <div class="brand-plate">
      <span class="brand-name">VELMORA</span>
    </div>
  </section>
</body>
</html>
```